Flyer für Vermietung und Verkauf von Hüpfburgen, aufblasbaren Festzelten und aufblasbaren Hindernisparcours
Zielgruppe
Wir vermieten und verkaufen Hüpfburgen, aufblasbare Festzelte und aufblasbare Hindernisparcours. Ebenso Sport- und Fungeräte mit Augmented Reality. Für den aktuelen Flyer sollen Vereine, Städte, Gemeinden und Private für den Fasching angesprochen werden.
Aufgabenstellung
Der Flyer soll A4 sein mit 6 Bildern.
Als Text soll enthalten sein:
Slogan: Ihre Faschingsparty mit unseren aufblasbaren Highlights (bessere Ideen sind gerne gefragt)
Text: Machen Sie mit unseren aufblasbaren Hinguckern Ihre Faschingsparty zum absoluten Highlight.
Ganz gleich, ob in der Firma oder privat, für jeden Anlass bieten wir die passende Ergänzung.
Spiele, Hüpfburgen, Sport-Parcours oder Festzelte mit Beleuchtung, wir bieten Ihnen unbegrenzte Möglichkeiten für Ihre Party.
Kontakt:
Bei Interesse kontaktieren Sie uns bitte via Email!
Renate Wolkner re.wolkner@pumpflor.biz
Seestadt (Germany) - Bergfeld (Austria)

```html
<!DOCTYPE html>
<html lang="de">
<head>
<meta charset="UTF-8">
<title>Fasching Flyer – pumpflor</title>
<link rel="stylesheet" href="https://fonts.googleapis.com/css2?family=Bebas+Neue&family=Poppins:wght@400;600&display=swap">
<style>
  :root {
    --brand-red: #e84343;
    --ink: #1d1d1b;
    --logo-grey: #3c3c3b;
    --paper: #ffffff;
  }
  * { margin: 0; padding: 0; box-sizing: border-box; }
  html, body { width: 849px; height: 1200px; overflow: hidden; background: var(--paper); }
  .flyer {
    position: relative;
    width: 849px;
    height: 1200px;
    overflow: hidden;
    background: var(--paper);
    font-family: "Poppins", sans-serif;
    color: var(--ink);
  }
  .brand {
    position: absolute;
    left: 60px;
    top: 80px;
    display: flex;
    align-items: center;
    gap: 14px;
  }
  .brand-dot {
    width: 30px;
    height: 30px;
    border-radius: 50%;
    background: var(--brand-red);
  }
  .brand-name {
    font-family: "Poppins", sans-serif;
    font-weight: 600;
    font-size: 38px;
    color: var(--logo-grey);
    letter-spacing: 0.5px;
  }
  .headline {
    position: absolute;
    left: 57px;
    top: 210px;
    font-family: "Bebas Neue", sans-serif;
    font-weight: 400;
    font-size: 44px;
    line-height: 53px;
    color: var(--brand-red);
    letter-spacing: 0.3px;
    white-space: nowrap;
  }
  .intro {
    position: absolute;
    left: 57px;
    top: 330px;
    font-weight: 600;
    font-size: 16px;
    line-height: 33px;
    color: var(--ink);
    white-space: nowrap;
  }
  .feature-art {
    position: absolute;
    left: 0;
    top: 0;
    width: 849px;
    height: 1200px;
  }
  .contact {
    position: absolute;
    right: 57px;
    top: 1030px;
    text-align: right;
    color: var(--paper);
    font-style: normal;
    font-weight: 400;
    font-size: 18px;
    line-height: 28.5px;
    white-space: nowrap;
  }
</style>
</head>
<body>
<main class="flyer">
  <header class="brand">
    <span class="brand-dot"></span>
    <span class="brand-name">pumpflor</span>
  </header>

  <h1 class="headline">Feiern Sie Fasching im Stil mit<br>unseren aufblasbaren Highlights</h1>

  <p class="intro">Machen Sie mit unseren aufblasbaren Hinguckern Ihre Fasching-<br>sparty zum absoluten Highlight. Ganz gleich, ob in der Firma oder<br>privat, für jeden Anlass bieten wir die passende Ergänzung. Spiele,<br>Hüpfburgen, Sport-Parcours oder Festzelte mit Beleuchtung, wir<br>bieten Ihnen unbegrenzte Möglichkeiten für Ihre Party.</p>

  <svg class="feature-art" viewBox="0 0 849 1200" xmlns="http://www.w3.org/2000/svg">
    <defs>
      <linearGradient id="castleTones" x1="0" y1="0" x2="0" y2="1">
        <stop offset="0" stop-color="#c9d3de"/>
        <stop offset="0.45" stop-color="#5aa83a"/>
        <stop offset="1" stop-color="#2f6e25"/>
      </linearGradient>
      <linearGradient id="towerTones" x1="0" y1="0" x2="0" y2="1">
        <stop offset="0" stop-color="#ffffff"/>
        <stop offset="0.5" stop-color="#d85a3c"/>
        <stop offset="1" stop-color="#e9b14a"/>
      </linearGradient>
      <linearGradient id="hutTones" x1="0" y1="0" x2="0" y2="1">
        <stop offset="0" stop-color="#ffffff"/>
        <stop offset="0.4" stop-color="#e9e6e3"/>
        <stop offset="0.65" stop-color="#8a6a55"/>
        <stop offset="1" stop-color="#ffffff"/>
      </linearGradient>
    </defs>

    <circle cx="214" cy="842" r="340" fill="var(--brand-red)"/>
    <rect x="0" y="850" width="849" height="350" fill="var(--brand-red)"/>
    <circle cx="613" cy="772" r="122" fill="var(--brand-red)"/>
    <circle cx="722" cy="828" r="136" fill="var(--brand-red)"/>

    <circle cx="214" cy="842" r="300" fill="url(#castleTones)" role="img" aria-label="Foto: grüne Hüpfburg mit Monsterfigur im Freien"/>
    <circle cx="613" cy="772" r="107" fill="url(#towerTones)" role="img" aria-label="Foto: aufblasbarer Feuerwehr-Kletterturm"/>
    <circle cx="722" cy="828" r="121" fill="url(#hutTones)" role="img" aria-label="Foto: aufblasbares Festzelt als verschneite Holzhütte"/>
  </svg>

  <address class="contact">
    Bei Interesse kontaktieren<br>
    Sie uns bitte via Email!<br>
    Renate Wolkner re.wolkner@pumpflor.biz<br>
    Seestadt (Germany) - Bergfeld (Austria)
  </address>
</main>
</body>
</html>
```